KVRo Business Cards

We need a business card design. We are a Technology (Audio Visual) design, sales and installation company. Looking for a double sided design, clean

Contact Information for Business Card

Clean, modern look, 2 sided

Font styles to use
Sans Serif

```html
<!DOCTYPE html>
<html lang="en">
<head>
<meta charset="utf-8">
<title>KVRo Business Card</title>
<link rel="stylesheet" href="https://fonts.googleapis.com/css2?family=Bitter:wght@400&family=Josefin+Sans:wght@600;700&display=swap">
<style>
  :root {
    --card-dark: #231f1e;
    --brand-orange: #f3960c;
    --paper-white: #ffffff;
    --rule-grey: #a8a39b;
    --text-light: #f4f2ee;
  }
  * { margin: 0; padding: 0; box-sizing: border-box; }
  html, body {
    width: 1200px; height: 384px; overflow: hidden;
    background: var(--paper-white);
  }
  .canvas { position: relative; width: 1200px; height: 384px; }

  /* Front side */
  .card-front-edge {
    position: absolute; left: 0; top: 0; width: 573px; height: 384px;
    background: var(--brand-orange);
  }
  .card-front {
    position: absolute; left: 0; top: 0; width: 566px; height: 378px;
    background: var(--card-dark);
  }
  .front-wordmark {
    position: absolute; left: 54px; top: 62px;
    font-family: "Josefin Sans", sans-serif; font-weight: 700;
    font-size: 60px; line-height: 1; color: var(--paper-white);
    letter-spacing: -1px;
  }
  .rule {
    position: absolute; left: 54px; width: 462px; height: 1px;
    background: var(--rule-grey);
  }
  .rule-top { top: 126px; }
  .rule-mid { top: 152px; }
  .rule-bottom { top: 175px; }
  .tagline {
    position: absolute; left: 54px;
    font-family: "Josefin Sans", sans-serif; font-weight: 600;
    font-size: 13px; line-height: 1; letter-spacing: 0.9px;
    color: var(--text-light); text-transform: uppercase; white-space: nowrap;
  }
  .tagline-first { top: 136px; }
  .tagline-second { top: 159px; }

  .contact-icon { position: absolute; left: 54px; width: 36px; height: 36px; }
  .icon-address { top: 204px; }
  .icon-reach { top: 259px; }

  .contact-block {
    position: absolute; left: 98px; top: 188px;
    font-family: "Bitter", serif; font-weight: 400;
    font-size: 21px; line-height: 22.6px; color: var(--text-light);
  }
  .contact-phone { font-size: 24px; line-height: 28px; }

  /* Back side */
  .card-back {
    position: absolute; left: 629px; top: 0; width: 571px; height: 384px;
    background: var(--brand-orange);
    display: flex; align-items: center; justify-content: center;
  }
  .back-wordmark {
    font-family: "Josefin Sans", sans-serif; font-weight: 700;
    font-size: 96px; line-height: 1; color: var(--paper-white);
    letter-spacing: -2px; padding-top: 14px; padding-left: 58px;
  }
</style>
</head>
<body>
<main class="canvas">
  <section class="card-front-edge" aria-hidden="true"></section>
  <section class="card-front">
    <div class="front-wordmark">KVRo</div>

    <div class="rule rule-top"></div>
    <p class="tagline tagline-first">Profesional audio ,vedio, lighting and automation</p>
    <div class="rule rule-mid"></div>
    <p class="tagline tagline-second">Equipment consulting, design and implementation</p>
    <div class="rule rule-bottom"></div>

    <svg class="contact-icon icon-address" viewBox="0 0 36 36" aria-hidden="true">
      <circle cx="18" cy="18" r="15.5" fill="none" stroke="#f3960c" stroke-width="3.2"/>
    </svg>
    <svg class="contact-icon icon-reach" viewBox="0 0 36 36" aria-hidden="true">
      <circle cx="18" cy="18" r="15.5" fill="none" stroke="#f3960c" stroke-width="3.2"/>
    </svg>

    <address class="contact-block" style="font-style: normal;">
      1840 Calloway Ct.<br>
      Suite 200<br>
      Dalton, Georgia 30720<br>
      sales@kvro.tech<br>
      <span class="contact-phone">(555)312-0148</span>
    </address>
  </section>

  <section class="card-back">
    <div class="back-wordmark">KVRo</div>
  </section>
</main>
</body>
</html>
```